Design Challege - Simplify a Complex Message

We have a new website design, but one of the pages presents a particular problem.

Our company does ERP implementations. We have developed a proprietary approach to these implementations based on the idea that you must get eight (and only eight) things right. These eight things are listed below, summarized in one or two words each:

1. Value
2. Capability
3. Functionality
4. Data
5. Technology
6. Change Leadership
7. Quality
8. Governance

Each of these eight things can be summarized in a short paragraph, but when you combine all eight summaries with a brief introductory text, the result is a lot of text - so much text that the casual surfer may be overwhelmed by it.

The winning design will find an engaging way to present the information in a way that presents a high-level summary, using icons and one- or two-word descriptions above but revealing more information when clicked.

Our current design for this information, with a paragraph describing the eight elements in a table, is included as an upload in PDF and Microsoft Word formats. We are looking for a creative way to display these eight things, showing the detail only when the user wants to see it.

The website is being built in WordPress, using Elementor as a page builder.

We will implement (code) the page, but the winner will be asked to specify the widget or other add-in if one is required.

The design does not need to include a header or footer, we have those.

Target Market(s)

Business executives working in technology

Industry/Entity Type

Any

Number of Pages Required

1 page

Font styles to use
Sans Serif

Requirements
Must have
• A design for the body of the page, but not the header or footer.
Nice to have
• Unique icons or images appropriate for each of the eight things.
Should not have
• A lot of text on one page

```html
<!DOCTYPE html>
<html lang="en">
<head>
<meta charset="utf-8">
<title>ERP Implementations – Eight Things to Get Right</title>
<link rel="stylesheet" href="https://fonts.googleapis.com/css2?family=Roboto:wght@300;400;500&family=Titillium+Web:wght@700;900&display=swap">
<style>
  :root {
    --bg: #f4f4f4;
    --ink: #111111;
    --text: #333333;
    --title: #222222;
    --link: #2a8be6;
    --sky: #5bcdfd;
    --blue: #2f9bf6;
    --accent: #fcdc78;
    --white: #ffffff;
  }
  html, body { margin: 0; padding: 0; overflow: hidden; background: var(--bg); }
  .page {
    position: relative; width: 1200px; height: 903px; overflow: hidden;
    background: var(--bg); font-family: "Roboto", Arial, sans-serif; color: var(--text);
  }
  .headline {
    position: absolute; top: 47px; left: 0; width: 1200px; margin: 0; text-align: center;
    font-family: "Titillium Web", Arial, sans-serif; font-weight: 900; font-size: 41px;
    line-height: 1; color: var(--ink); letter-spacing: 0.3px;
  }
  .subhead {
    position: absolute; top: 92px; left: 0; width: 1200px; margin: 0; text-align: center;
    font-weight: 300; font-size: 24px; line-height: 28px; color: var(--sky);
  }
  .intro {
    position: absolute; top: 131px; left: 262px; width: 686px; margin: 0; text-align: center;
    font-weight: 300; font-size: 12.2px; line-height: 18px; color: #444;
  }
  .diagram { position: absolute; inset: 0; width: 1200px; height: 903px; }
  .hub-art {
    position: absolute; left: 475px; top: 346px; width: 236px; height: 236px; border-radius: 50%;
    background: radial-gradient(circle at 50% 45%, #bfe6ff 0%, #7cc6fb 38%, #eaf6ff 70%, #ffffff 100%);
  }

  .pillar summary { list-style: none; cursor: pointer; }
  .pillar summary::-webkit-details-marker { display: none; }
  .pillar summary:focus-visible .pillar-title { outline: 2px solid var(--blue); outline-offset: 3px; }
  .pillar[open] .pillar-title, .pillar summary:hover .pillar-title { color: var(--blue); }

  .badge { position: absolute; width: 54px; height: 54px; border-radius: 50%; background: var(--accent); }
  .badge svg { position: absolute; left: -8px; top: 10px; width: 40px; height: 40px; }
  .pillar-title {
    position: absolute; margin: 0; font-weight: 500; font-size: 16px; line-height: 19px;
    color: var(--title); white-space: nowrap;
  }
  .pillar-text { position: absolute; margin: 0; font-size: 8.9px; line-height: 14.2px; color: var(--text); }
  .pillar-text a { color: var(--link); text-decoration: none; }
  .needs { list-style: none; margin: 5px 0 0; padding: 0; width: 400px; }
  .needs li { position: relative; padding-left: 12px; line-height: 14.8px; white-space: nowrap; }
  .needs li::before {
    content: ""; position: absolute; left: 1px; top: 4px; width: 5px; height: 5px;
    border: 1.2px solid #333; border-radius: 50%;
  }
  .more { display: block; margin-top: 4px; }
</style>
</head>
<body>
<main class="page">
  <h1 class="headline">ERP IMPLEMENTATIONS</h1>
  <p class="subhead">Eight Things to Get Right</p>
  <p class="intro">In an ERP implementation, you must get eight major things right to be successful. Ignore any of them, and your implementation will fail. Get them right, and you will likely succeed.</p>

  <svg class="diagram" viewBox="0 0 1200 903" aria-hidden="true">
    <defs>
      <linearGradient id="ringShade" x1="0" y1="0" x2="0" y2="1">
        <stop offset="0" stop-color="#5bcdfd"/>
        <stop offset="1" stop-color="#2f95f4"/>
      </linearGradient>
    </defs>
    <g fill="none" stroke-width="4.5" stroke-linecap="round">
      <path d="M384 257 H458 Q470 257 480 266 L555 352" stroke="#56c8fc"/>
      <path d="M802 257 H716 Q704 257 694 266 L629 335" stroke="#56c8fc"/>
      <path d="M290 410 H387 L477 426" stroke="#4dbdfb"/>
      <path d="M900 419 H800 L710 431" stroke="#4dbdfb"/>
      <path d="M297 572 H387 Q397 572 405 567 L474 526" stroke="#3badf8"/>
      <path d="M884 582 H787 Q777 582 768 576 L703 529" stroke="#3badf8"/>
      <path d="M415 705 H490 Q520 705 527 680 L555 580" stroke="#339ff6"/>
      <path d="M760 710 H684 Q655 710 648 686 L622 580" stroke="#339ff6"/>
    </g>
    <g fill="#4fc4fc">
      <rect x="354" y="223" width="27" height="64"/>
      <rect x="805" y="223" width="27" height="64"/>
      <rect x="262" y="379" width="27" height="64" fill="#45b9fb"/>
      <rect x="900" y="389" width="27" height="64" fill="#45b9fb"/>
      <rect x="270" y="542" width="27" height="63" fill="#3aabf8"/>
      <rect x="884" y="553" width="27" height="63" fill="#3aabf8"/>
      <rect x="388" y="677" width="27" height="64" fill="#339ff6"/>
      <rect x="760" y="681" width="27" height="64" fill="#339ff6"/>
    </g>
    <circle cx="593" cy="464" r="133" fill="none" stroke="url(#ringShade)" stroke-width="22"/>
    <g stroke="var(--bg)" stroke-width="5">
      <line x1="561" y1="335" x2="553" y2="318"/>
      <line x1="624" y1="335" x2="632" y2="318"/>
      <line x1="467" y1="425" x2="449" y2="420"/>
      <line x1="719" y1="432" x2="737" y2="428"/>
      <line x1="480" y1="522" x2="463" y2="530"/>
      <line x1="707" y1="520" x2="723" y2="528"/>
      <line x1="557" y1="590" x2="553" y2="607"/>
      <line x1="626" y1="590" x2="631" y2="607"/>
    </g>
    <circle cx="593" cy="464" r="119" fill="#ffffff" stroke="#cde9fb" stroke-width="2"/>
  </svg>

  <div class="hub-art" role="img" aria-label="Illustration of a small team working around a large ERP dashboard with charts"></div>

  <details class="pillar" name="pillars">
    <summary>
      <span class="badge" style="left:277px;top:206px">
        <svg viewBox="0 0 40 40" fill="none" stroke="#111" stroke-width="1.6" stroke-linejoin="round"><rect x="4" y="30" width="4" height="6"/><rect x="11" y="26" width="4" height="10"/><rect x="18" y="22" width="4" height="14"/><rect x="25" y="17" width="4" height="19"/><rect x="32" y="12" width="4" height="24"/><path d="M3 26 L14 17 L20 20 L35 5 M30 5 H35 V10"/><circle cx="17" cy="9" r="5"/><path d="M17 6 V12 M15.5 7.5 H18 M15.5 10.5 H18.5"/></svg>
      </span>
      <span class="pillar-title" style="left:287px;top:269px">Value</span>
    </summary>
    <p class="pillar-text" style="left:108px;top:296px;width:362px">The project must provide value that significantly exceeds potential project costs and should be aligned with the company’s strategy. Its value and strategic alignment must be part of a vision shared by the company’s leadership. Value from the project must be delivered in a way that respects resource constraints. <a href="#">Learn More</a></p>
  </details>

  <details class="pillar" name="pillars">
    <summary>
      <span class="badge" style="left:866px;top:215px">
        <svg viewBox="0 0 40 40" fill="none" stroke="#111" stroke-width="1.6" stroke-linejoin="round"><path d="M4 13 L20 3 L36 13 Z"/><circle cx="20" cy="9" r="1.5"/><rect x="5" y="13" width="30" height="3"/><path d="M9 16 V31 M13 16 V31 M18 16 V31 M22 16 V31 M27 16 V31 M31 16 V31"/><rect x="5" y="31" width="30" height="3"/><rect x="3" y="34" width="34" height="3"/></svg>
      </span>
      <span class="pillar-title" style="left:863px;top:272px">Governance</span>
    </summary>
    <p class="pillar-text" style="left:740px;top:297px;width:345px">The project must provide value that significantly exceeds potential project costs and should be aligned with the company’s strategy. Its value and strategic alignment must be part of a vision shared by the company’s leadership. Value from the project must be delivered in a way that respects resource constraints. <a href="#">Learn More</a></p>
  </details>

  <details class="pillar" name="pillars">
    <summary>
      <span class="badge" style="left:182px;top:367px">
        <svg viewBox="0 0 40 40" fill="none" stroke="#111" stroke-width="1.6" stroke-linejoin="round"><circle cx="14" cy="6" r="3.5"/><path d="M8 24 V14 Q8 11 11 11 H17 Q20 11 20 14 V24 M11 18 V36 M17 18 V36 M14 24 V36"/><circle cx="32" cy="6" r="2.5"/><circle cx="36" cy="20" r="2.5"/><circle cx="32" cy="34" r="2.5"/><path d="M20 20 H33.5 M20 16 L30 8 M20 24 L30 32"/></svg>
      </span>
      <span class="pillar-title" style="left:168px;top:427px">Capability</span>
    </summary>
    <div class="pillar-text" style="left:41px;top:451px;width:318px">
      <p style="margin:0">The company and the implementation team must be capable of implementing the project on their own or with help. The project must have the following:</p>
      <ul class="needs">
        <li>Resources required, including people, time, and budget.</li>
        <li>Processes required, usually delivered through a comprehensive methodology.</li>
        <li>Prioritization required because an ERP project will need the commitment of the entire company.</li>
      </ul>
      <a class="more" href="#">Learn More</a>
    </div>
  </details>

  <details class="pillar" name="pillars">
    <summary>
      <span class="badge" style="left:947px;top:381px">
        <svg viewBox="0 0 40 40" fill="none" stroke="#111" stroke-width="1.6" stroke-linejoin="round" style="left:0;top:7px"><path d="M20 3 L24 6 L29 5 L31 10 L36 12 L35 17 L38 21 L35 25 L36 30 L31 31 L29 36 L24 35 L20 38 L16 35 L11 36 L9 31 L4 30 L5 25 L2 21 L5 17 L4 12 L9 10 L11 5 L16 6 Z"/><circle cx="20" cy="21" r="10"/><path d="M15 21 L19 25 L26 17"/></svg>
      </span>
      <span class="pillar-title" style="left:953px;top:438px">Quality</span>
    </summary>
    <p class="pillar-text" style="left:807px;top:463px;width:342px">The project must provide value that significantly exceeds potential project costs and should be aligned with the company’s strategy. Its value and strategic alignment must be part of a vision shared by the company’s leadership. Value from the project must be delivered in a way that respects resource constraints. <a href="#">Learn More</a></p>
  </details>

  <details class="pillar" name="pillars">
    <summary>
      <span class="badge" style="left:188px;top:539px">
        <svg viewBox="0 0 40 40" fill="none" stroke="#111" stroke-width="1.6" stroke-linejoin="round" style="left:6px;top:7px"><path d="M17 3 H23 L24 8 L28 10 L33 7 L37 12 L33 16 L34 20 L38 22 V27 L33 28 L31 32 L34 36 L29 40 L25 36 L21 37 L19 42 M17 3 L16 8 L12 10 L7 7 L3 12 L7 16 L6 20 L2 22 V27 L7 28 L9 32 L6 36 L11 40 L15 36 L19 37" transform="scale(0.9) translate(2,0)"/><circle cx="20" cy="20" r="7"/></svg>
      </span>
      <span class="pillar-title" style="left:151px;top:595px">Functionality</span>
    </summary>
    <p class="pillar-text" style="left:90px;top:617px;width:345px">An ERP project must support required business processes, both now and in the future. A systematic review of all business processes and how they will be supported, either by the system or otherwise, is crucial. <a href="#">Learn More</a></p>
  </details>

  <details class="pillar" name="pillars">
    <summary>
      <span class="badge" style="left:934px;top:543px">
        <svg viewBox="0 0 40 40" fill="none" stroke="#111" stroke-width="1.6" stroke-linejoin="round" style="left:0;top:6px"><path d="M13 22 V14 Q13 12 15 12 Q17 12 17 14 V13 Q17 11 19 11 Q21 11 21 13 Q21 11 23 11 Q25 11 25 13 Q25 11.5 27 11.5 Q29 11.5 29 13.5 V24 Q29 29 25 31 V37 H15 V31 Q11 29 11 24 V22 Q11 20 13 20 H19 Q21 20 21 22 Q21 24 19 24 H16"/><path d="M20 3 V7 M11 5 L13 8 M29 5 L27 8 M4 14 H8 M32 14 H36"/></svg>
      </span>
      <span class="pillar-title" style="left:940px;top:600px">Change Leadership</span>
    </summary>
    <p class="pillar-text" style="left:808px;top:625px;width:364px">Change leadership (often called change management) considers the human side of an ERP implementation. Change is hard, even if it’s a good change. Training is an important element of change leadership. But beyond training, consideration must be given to the people using the system. How are they involved in communication and important. <a href="#">Learn More</a></p>
  </details>

  <details class="pillar" name="pillars">
    <summary>
      <span class="badge" style="left:310px;top:668px">
        <svg viewBox="0 0 40 40" fill="none" stroke="#111" stroke-width="1.6" stroke-linejoin="round" style="left:12px;top:8px"><ellipse cx="20" cy="7" rx="14" ry="4"/><path d="M6 7 V33 Q6 37 20 37 Q34 37 34 33 V7 M6 14 Q6 18 20 18 Q34 18 34 14 M6 21 Q6 25 20 25 Q34 25 34 21 M6 28 Q6 32 20 32 Q34 32 34 28"/><path d="M10 12 V15 M10 19 V22 M10 26 V29"/></svg>
      </span>
      <span class="pillar-title" style="left:323px;top:727px">Data</span>
    </summary>
    <p class="pillar-text" style="left:228px;top:754px;width:345px">ERP systems are data-hungry creatures. Please be careful before assuming that because so much data goes into them, an equal amount of insight will emerge. Getting data right means considering data architecture, migration, integration, governance, and, perhaps most importantly, access. <a href="#">Learn More</a></p>
  </details>

  <details class="pillar" name="pillars">
    <summary>
      <span class="badge" style="left:814px;top:689px">
        <svg viewBox="0 0 40 40" fill="none" stroke="#111" stroke-width="1.6" stroke-linejoin="round" style="left:-6px;top:8px"><circle cx="16" cy="14" r="11"/><circle cx="16" cy="14" r="7"/><circle cx="16" cy="14" r="3"/><path d="M14 18 V30 L11 27 Q9 26 8 28 L14 37 H28 Q31 32 31 27 V22 Q31 20 29 20 Q27 20 27 22 Q27 19 25 19 Q23 19 23 21 Q23 18.5 21 18.5 Q19 18.5 19 20.5 V14 Q19 12 16.5 12 Q14 12 14 14 Z"/><path d="M22 2 V4"/></svg>
      </span>
      <span class="pillar-title" style="left:814px;top:747px">Technology</span>
    </summary>
    <p class="pillar-text" style="left:680px;top:771px;width:345px">What is the platform for the system? Is it offered by a vendor that will be around for as long as your system? Will it integrate with your other systems? Are resources available to support it? Can you change it without painting yourself into a corner? Will your technology scale as you grow? <a href="#">Learn More</a></p>
  </details>
</main>
</body>
</html>
```